Redesign Gearcrate.co.uk website for Film,Tv & Photo Industries.

www.gearcrate.co.uk needs a major redesign and new fresh look.
We will be using Quillbrook V1 software and have a company that will do all the coding etc etc.

The website is for people who work in the film, tv and photographic industries and are looking to buy bags and cases for their equipment.
About 14 different Manufacturers will be featured.
Just need a modern home page, everything else will follow this design.
Updates

Hi All, I have altered the description of the project , not that much has altered just giving more info out. regards Rob Calder.

Hi Everyone, I have just uploaded a new logo for the www.gearcrate.co.uk website. regards Rob Calder.

Final logo has been uploaded. Regards Rob.

Reason: Even though there are many good designs a lot of them are the same. I would like to see even more of a modern design even using flat colours that don't follow the colour of the new logo regards Rob.

Having seen many very good designs I would like to see different designs using FLAT colours which are modern . You don't have to stick to the colours of the logo as i can change the red in the logo to match the colour of the website. regards Rob Calder.

Target Market(s)

Artistic People who work in Film , TV and photographic Industries. Photographers, cameramen, Production Companies who need to protect their equipment.
Both Pro and Amateur.

Industry/Entity Type

Software

Requirements
Must have
• open minded
Nice to have
• Modern Look

```html
<!DOCTYPE html>
<html lang="en">
<head>
<meta charset="utf-8">
<title>Gearcrate – Bags &amp; Cases for Film, TV &amp; Photo</title>
<link href="https://fonts.googleapis.com/css2?family=Ubuntu:wght@400;500;700&family=Open+Sans:wght@400;600&display=swap" rel="stylesheet">
<style>
:root{
  --red:#d6151b;
  --red-dark:#b50f14;
  --ink:#333;
  --muted:#666;
  --line:#e3e3e3;
  --panel:#f5f5f5;
  --footer:#f3f3f3;
  --footer-base:#ececec;
  --dark:#3b3b3b;
}
*{margin:0;padding:0;box-sizing:border-box}
html,body{width:749px;height:1200px;overflow:hidden;background:#fff}
body{position:relative;font-family:"Open Sans",sans-serif;color:var(--ink)}
.abs{position:absolute}
.top-band{left:0;top:0;width:749px;height:131px;background:linear-gradient(#fdfdfd,#d9d9d9)}
.logo{left:80px;top:14px;display:flex;align-items:center;gap:6px}
.logo-mark{width:40px;height:40px;border-radius:50%;background:linear-gradient(#6a6a6a,#222)}
.logo-name{font-family:"Ubuntu",sans-serif;font-size:20px;color:#555}
.cart{left:607px;top:12px;display:flex;gap:5px;align-items:flex-start}
.cart-label{font-size:7px;color:#555;line-height:1.2}
.cart-count{font-size:12px;color:var(--red);display:block}
.search{left:531px;top:41px;width:143px;height:18px;background:#fff;border-radius:9px;border:1px solid #ddd;font-size:6.5px;color:#999;padding:4px 9px}
.search svg{position:absolute;right:6px;top:3px}
.nav{left:76px;top:66px;width:597px;height:30px;background:var(--red);display:flex}
.nav span{font-family:"Ubuntu",sans-serif;font-weight:500;font-size:9.5px;color:#fff;text-align:center;line-height:30px;border-right:1px solid #b70d12}
.nav span:last-child{border:none}
.hero{left:76px;top:95px;width:597px;height:253px;background:linear-gradient(100deg,#9cc0de 0%,#b9cfe0 40%,#6f7378 60%,#b8322b 75%,#3e3e40 100%)}
.hero-box{left:106px;top:177px;width:252px;height:94px;background:rgba(60,60,60,.88);padding:14px 16px;color:#fff}
.hero-kicker{font-family:"Ubuntu",sans-serif;font-size:12px}
.hero-title{font-family:"Ubuntu",sans-serif;font-weight:500;font-size:20px;margin-top:1px}
.hero-text{font-size:6.6px;line-height:1.7;color:#ddd;margin-top:3px}
.dots{left:355px;top:332px;display:flex;gap:4px}
.dots i{width:7px;height:7px;border-radius:50%;background:#fff}
.tile{top:360px;width:195px;height:106px}
.tile-caption{position:absolute;left:0;bottom:0;width:100%;height:28px;background:rgba(214,21,27,.85);color:#fff;font-family:"Ubuntu",sans-serif;font-size:12px;text-align:center;line-height:28px}
.tile.grey .tile-caption{background:rgba(90,90,90,.85)}
.side-head{width:136px;height:28px;background:linear-gradient(#6a6a6a,#3e3e3e);color:#fff;font-family:"Ubuntu",sans-serif;font-weight:500;font-size:11.5px;padding-left:17px;line-height:28px}
.side-list{width:136px;background:var(--panel);padding:4px 12px 4px 12px;border:1px solid #eee;border-top:none}
.side-list li{list-style:none;font-size:7.4px;color:#555;height:17px;line-height:17px;border-bottom:1px solid var(--line);position:relative;padding-left:7px}
.side-list li:last-child{border:none}
.side-list li::after{content:"";position:absolute;right:2px;top:6px;width:4px;height:4px;border-right:1px solid #aaa;border-top:1px solid #aaa;transform:rotate(45deg)}
.ship{left:78px;top:830px;width:136px;height:154px;background:linear-gradient(#d81b20,#b40f14);color:#fff;text-align:center;padding-top:14px}
.ship-title{font-family:"Ubuntu",sans-serif;font-weight:500;font-size:14px;margin-top:4px}
.ship-sub{font-family:"Ubuntu",sans-serif;font-weight:500;font-size:8.5px}
.ship-text{font-size:6.6px;line-height:1.75;margin-top:5px;padding:0 12px}
.welcome{left:234px;top:497px;font-family:"Ubuntu",sans-serif;font-weight:500;font-size:16px;color:var(--red)}
.intro{left:236px;top:522px;width:430px;font-size:7.8px;line-height:14.6px;color:#555}
.intro p+p{margin-top:1.5px}
.featured{left:235px;top:635px;font-family:"Ubuntu",sans-serif;font-size:13px;color:#444}
.card{width:139px;height:158px;border:1px solid #e2e2e2;border-radius:3px;background:#fff}
.card .ph{position:absolute;left:40px;top:14px;width:58px;height:70px;border-radius:4px}
.card .name{position:absolute;left:13px;top:113px;font-family:"Ubuntu",sans-serif;font-size:9.5px;color:#555}
.card .price{position:absolute;left:13px;top:131px;font-family:"Ubuntu",sans-serif;font-size:12px;color:#222}
.card .btn{position:absolute;left:71px;top:132px;width:59px;height:16px;background:var(--red);color:#fff;font-size:7.5px;text-align:center;line-height:16px}
.footer{left:0;top:1016px;width:749px;height:148px;background:var(--footer)}
.footer-base{left:0;top:1164px;width:749px;height:36px;background:var(--footer-base)}
.fcol h4{font-family:"Ubuntu",sans-serif;font-weight:400;font-size:12px;color:#444;margin-bottom:4px}
.fcol h4.spaced{font-weight:500;font-size:9.5px;letter-spacing:1px;margin-bottom:7px}
.fcol a{display:block;font-size:7.8px;color:#555;line-height:15px;text-decoration:none}
.fcol p{font-size:6.8px;color:#555}
.vline{top:1046px;width:1px;height:80px;background:#ddd}
.email{width:139px;height:18px;background:#fff;border:1px solid #ccc;font-size:6.4px;color:#aaa;padding:4px 6px;margin-top:6px}
.sub-btn{width:66px;height:18px;background:var(--dark);color:#fff;font-size:8.5px;text-align:center;line-height:18px;margin-top:6px}
.socials{display:flex;gap:3px;margin-top:6px}
.socials i{width:17px;height:17px;border-radius:50%;background:#111}
.copy{left:76px;top:1179px;font-size:7px;color:#666}
.pay{left:559px;top:1177px;display:flex;gap:3px}
.pay i{width:20px;height:13px;border:1px solid #999;background:#fff}
.pay i.wide{width:36px}
</style>
</head>
<body>
<div class="abs top-band"></div>

<div class="abs logo"><div class="logo-mark"></div><span class="logo-name">Gearcrate</span></div>

<div class="abs cart">
  <svg width="20" height="17" viewBox="0 0 20 17"><path d="M1 2h3l3 9h10l2-6H6" fill="none" stroke="#d6151b" stroke-width="1.8"/><circle cx="8" cy="14.5" r="1.6" fill="#d6151b"/><circle cx="16" cy="14.5" r="1.6" fill="#d6151b"/></svg>
  <div class="cart-label">Checkout<span class="cart-count">0 items</span></div>
</div>
<div class="abs search">Search here..
  <svg width="10" height="10" viewBox="0 0 10 10"><circle cx="4" cy="4" r="3" fill="none" stroke="#aaa"/><path d="M6.2 6.2L9 9" stroke="#aaa"/></svg>
</div>

<nav class="abs nav">
  <span style="width:71px">HOME</span>
  <span style="width:76px">ABOUT US</span>
  <span style="width:78px">PRODUCTS</span>
  <span style="width:91px">MY ACCOUNT</span>
  <span style="width:108px">SPECIAL OFFERS</span>
  <span style="width:69px">SUPPORT</span>
  <span style="width:104px">CONTACT</span>
</nav>

<div class="abs hero" role="img" aria-label="Photographer with a red backpack shooting by the sea"></div>
<div class="abs hero-box">
  <div class="hero-kicker">Mauris vel lacus vitae vestibulum</div>
  <div class="hero-title">Etiam estnunc venenat</div>
  <div class="hero-text">Integer orci tellus tristique vitae consequat nec porta vel<br>lectus Nulla sit amet diam Duis non nunc</div>
</div>
<div class="abs dots"><i></i><i></i><i></i><i></i></div>

<div class="abs tile" style="left:76px;background:linear-gradient(135deg,#c62026,#3a3a3a 60%,#b81c22)" role="img" aria-label="Camera gear in a red case"><div class="tile-caption">LATEST ARRIVALS BAGS</div></div>
<div class="abs tile grey" style="left:278px;background:linear-gradient(135deg,#e4e4dc,#6f7256 55%,#c9c9c0)" role="img" aria-label="Green canvas camera bag"><div class="tile-caption">LATEST ARRIVALS BAGS</div></div>
<div class="abs tile" style="left:478px;background:linear-gradient(135deg,#b7c2c8,#d6d8d9 45%,#2b2b2d)" role="img" aria-label="Black shoulder bag carried at an airport"><div class="tile-caption">LATEST ARRIVALS BAGS</div></div>

<div class="abs" style="left:76px;top:493px">
  <div class="side-head">Broadcast</div>
  <ul class="side-list">
    <li>Fieldmate</li><li>Stonebrace</li><li>Ridgeline - Storm Cases</li><li>Ridgeline</li><li>Norvik</li><li>Copperline</li><li>Keystone Cases</li>
  </ul>
</div>
<div class="abs" style="left:78px;top:658px">
  <div class="side-head">Photography</div>
  <ul class="side-list">
    <li>Fieldmate</li><li>Stonebrace</li><li>Ridgeline - Storm Cases</li><li>Ridgeline</li><li>Norvik</li><li>Copperline</li><li>Keystone Cases</li>
  </ul>
</div>

<div class="abs ship">
  <svg width="60" height="52" viewBox="0 0 60 52">
    <circle cx="24" cy="24" r="20" fill="none" stroke="#fff" stroke-width="3"/>
    <ellipse cx="24" cy="24" rx="9" ry="20" fill="none" stroke="#fff" stroke-width="2.5"/>
    <path d="M4 24h40M7 14h34M7 34h34" stroke="#fff" stroke-width="2.5"/>
    <rect x="30" y="30" width="18" height="13" fill="#fff"/>
    <path d="M48 34h6l4 5v4H48z" fill="#fff"/>
    <circle cx="35" cy="45" r="3.5" fill="#fff" stroke="#c3151a" stroke-width="1.5"/>
    <circle cx="52" cy="45" r="3.5" fill="#fff" stroke="#c3151a" stroke-width="1.5"/>
  </svg>
  <div class="ship-title">FREE SHIPPING</div>
  <div class="ship-sub">OVER $150 PRICE</div>
  <div class="ship-text">Mauris vel lacus vitae felis vestibulum volutpat Etiam est nunc venenatis in tristique</div>
</div>

<h1 class="abs welcome">WELCOME TO OUR WEBSITE MAINPAGE</h1>
<div class="abs intro">
  <p>Gearcrate are a leading distributor to the film, television and photographic industries. We stock thousands of quality products from Ridgeline, Bramblewood, Ashcombe, Norvik, Feldor, Trevan, Halloway, Copperline, Stonebrace, Lumaro, Harlow, Vistel and other leading manufacturers. These products include:</p>
  <p>Ridgeline camera cases, Ridgeline director cases, Ridgeline projector cases and Ridgeline audio cases</p>
  <p>Bramblewood camera cases, Bramblewood laptop bags and Bramblewood bags</p>
  <p>Ashcombe camera bags, Ashcombe pockets and Ashcombe stowaway bags</p>
</div>

<h2 class="abs featured">FEATURED PRODUCTS</h2>

<div class="abs card" style="left:234px;top:659px"><div class="ph" style="background:linear-gradient(#555,#222)" role="img" aria-label="Rolling hard case"></div><span class="name">Product Name</span><span class="price">$203.47</span><span class="btn">Add to Cart</span></div>
<div class="abs card" style="left:382px;top:659px"><div class="ph" style="top:30px;height:36px;background:linear-gradient(#2a54b8,#1a2a55)" role="img" aria-label="Blue padded bag"></div><span class="name">Product Name</span><span class="price">$203.47</span><span class="btn">Add to Cart</span></div>
<div class="abs card" style="left:529px;top:659px"><div class="ph" style="background:linear-gradient(135deg,#2a2a2a,#c9a12a 50%,#1e1e1e)" role="img" aria-label="Open camera backpack"></div><span class="name">Product Name</span><span class="price">$203.47</span><span class="btn">Add to Cart</span></div>
<div class="abs card" style="left:236px;top:829px"><div class="ph" style="top:24px;height:50px;background:linear-gradient(#3a3a3a,#111)" role="img" aria-label="Open laptop case"></div><span class="name">Product Name</span><span class="price">$203.47</span><span class="btn">Add to Cart</span></div>
<div class="abs card" style="left:383px;top:829px"><div class="ph" style="top:26px;height:46px;background:linear-gradient(#4a4d55,#1c1d22)" role="img" aria-label="Black shoulder bag"></div><span class="name">Product Name</span><span class="price">$203.47</span><span class="btn">Add to Cart</span></div>
<div class="abs card" style="left:530px;top:829px"><div class="ph" style="top:24px;left:44px;width:50px;height:50px;background:linear-gradient(#3a3a3a,#151515)" role="img" aria-label="Small hard case"></div><span class="name">Product Name</span><span class="price">$203.47</span><span class="btn">Add to Cart</span></div>

<footer>
  <div class="abs footer"></div>
  <div class="abs fcol" style="left:76px;top:1040px"><h4>Company</h4><a>Contact Us</a><a>About Us</a><a>Blog</a><a>Career</a></div>
  <div class="abs vline" style="left:145px"></div>
  <div class="abs fcol" style="left:166px;top:1041px"><h4>Resources</h4><a>Shipping &amp; Delivery</a><a>Bulk Enquiry</a><a>FAQ</a><a>Advanced Search</a></div>
  <div class="abs vline" style="left:262px"></div>
  <div class="abs fcol" style="left:281px;top:1040px"><h4>Support</h4><a>My Account</a><a>FAQ</a><a>Support</a><a>Contact</a></div>
  <div class="abs vline" style="left:357px"></div>
  <div class="abs fcol" style="left:389px;top:1043px"><h4 class="spaced">Newsletter Subscribe</h4><p>We promise to only send you good things.</p><div class="email">Email address</div><div class="sub-btn">Subscribe</div></div>
  <div class="abs vline" style="left:552px"></div>
  <div class="abs fcol" style="left:573px;top:1043px"><h4 class="spaced">Follow Us</h4><p>Get Connect with us on these</p><div class="socials"><i></i><i></i><i></i><i></i></div></div>
  <div class="abs footer-base"></div>
  <div class="abs copy">Copyright © 2014 Northvale Trading | All Rights Reserved</div>
  <div class="abs pay"><i></i><i></i><i></i><i class="wide"></i></div>
</footer>
</body>
</html>
```